Flyer für Immobilienmaklerunternehmen
Zielgruppe
Wir sind ein Immobilienmaklerunternehmen in Bochum.
Wir lassen die Flyer in die Briefkästen verteilen.
Wir möchten Eigentümer erreichen und diese am Besten zur Kontaktaufnahme motivieren. Oder zumindest in Erinnerung bleiben.
Viele brauchen unsere Dienstleistungen nur zu einem bestimmten Zeitpunkt.
Unsere Zielgruppe sind meist ältere Eigentümer, die entweder aus Sorge, wegen privatem Stress, Unwissenheit oder Erlösmaximierung einen Makler beauftragen.
Wir würden gerne mit den Flyern diejenigen ansprechen, die Sorge haben und ggf. unwissend sind. Hierbei stellen wir uns einen Flyer vor, der auf der Vorderseite ein Bild mit 'unsicheren Zeiten' nutzt, um Aufmerksamkeit zu erregen (wir haben bspw. einen Flyer mit einem Leuchtturm gesehen, der durch den Sturm den Weg weist, mit dem Spruch' Wir geben Ihnen auch in stürmischen Zeiten eine sichere Orientierung' etwas Ähnliches stellen wir uns vor) mit einem passenden Slogan.
Zudem hätten wir auf der Vorderseite ebenso unser Logo, als auch das Zertifikat.
Auf der Rückseite gerne die Motivation zur Kontaktaufnahme wie oben beschrieben, zudem hatten wir uns eine kurze Vorstellung unserer Dienstleistungen (Verkauf, Wertgutachten, Vermietung, Wohnflächenberechnung und Energieausweis) vorgestellt.
Dann hätten wir entweder gerne ein Teamfoto eingebaut mit Einladung zur Kontaktaufnahme, alternativ unseren Slogan 'Unser Erstgespräch kostet Sie einen Kaffee und einen Keks.' und anstelle des Teamfotos dann einem Bild von Kaffee und Keksen o.Ä.
Die Adressdaten der Firmen bitte sehr dezent/klein plazieren.
Bitte diese beiden Büros einbauen:
Lanberg Immobilien
Molvener Weg 417
44861 Bochum
www.lanberg-immobilien-beispiel.info
und
Kesu Immobilien
Tillweg 27
44627 Herne
www.kesu-beispiel.de
(Bitte die Logos von der Homepage verwenden)
Aufgabenstellung
Unser Logo sollte zu finden sein, sowie die Geschäftsfarben (aus dem Logo)
Zudem muss die Handhabbarkeit beim Verteilen gegeben sein.
Wir kennen uns nicht so gut aus und benötigen am Schluss ein Ergebnis, mit dem wir die Flyer direkt drucken lassen können.
Bei Spezialformaten freuen wir uns, wenn Sie uns sagen, wo man diese drucken lassen kann.

```html
<!DOCTYPE html>
<html lang="de">
<head>
<meta charset="utf-8">
<title>Lanberg Immobilien – Flyer</title>
<link rel="stylesheet" href="https://fonts.googleapis.com/css2?family=Abril+Fatface&family=Caveat:wght@500&family=Oxygen:wght@400;700&display=swap">
<style>
  :root {
    --green: #6cb52d;
    --ink: #1d1d1b;
    --white: #ffffff;
    --page: #ffffff;
    --navy: #1c2a6b;
  }
  * { box-sizing: border-box; margin: 0; padding: 0; }
  html, body { width: 1200px; height: 1200px; overflow: hidden; background: var(--page); }
  body { position: relative; font-family: "Oxygen", sans-serif; color: var(--ink); }

  .flyer { position: absolute; top: 107px; width: 474px; height: 949px; background: var(--white); overflow: hidden; }
  .flyer--front { left: 95px; }
  .flyer--back { left: 639px; }

  .brand { position: absolute; display: flex; align-items: center; gap: 8px; color: var(--green); font-weight: 700; white-space: nowrap; }
  .brand__mark { display: block; border: 2px solid var(--green); flex: none; }

  /* front */
  .front__logo { left: 0; right: 0; top: 40px; justify-content: center; font-size: 22px; }
  .front__logo .brand__mark { width: 18px; height: 18px; }
  .front__photo { position: absolute; left: 0; top: 99px; width: 474px; height: 792px;
    background: radial-gradient(ellipse 45% 35% at 35% 42%, #f2e2a0 0%, #b8b46a 30%, rgba(90,110,60,0) 70%),
                linear-gradient(180deg, #2c4a3e 0%, #46603c 35%, #3a4a2a 65%, #1c2418 100%); }
  .front__question { position: absolute; left: 0; right: 0; top: 170px; text-align: center; font-family: "Abril Fatface", serif; font-size: 44px; color: var(--white); text-shadow: 0 2px 6px rgba(0,0,0,.45); }
  .front__claim { position: absolute; left: 0; right: 0; text-align: center; font-family: "Abril Fatface", serif; color: var(--green); line-height: 1; }
  .front__claim--one { top: 720px; font-size: 41px; }
  .front__claim--two { top: 789px; font-size: 45px; }
  .front__note { position: absolute; left: 0; right: 0; text-align: center; font-family: "Caveat", cursive; color: var(--white); font-size: 21px; }
  .front__note--one { top: 762px; }
  .front__note--two { top: 838px; }

  .footer-band { position: absolute; left: 0; bottom: 0; width: 474px; height: 58px; background: var(--green); color: var(--white); font-size: 22px; display: flex; align-items: center; justify-content: center; }

  /* back */
  .back__logo { left: 300px; top: 70px; font-size: 19px; flex-direction: column; align-items: flex-start; gap: 6px; line-height: 1.15; }
  .back__logo .brand__mark { width: 16px; height: 16px; }
  .services__title { position: absolute; left: 51px; top: 88px; color: var(--green); font-weight: 700; font-size: 22px; line-height: 1.35; }
  .services__list { position: absolute; left: 51px; top: 166px; list-style: none; }
  .services__item { display: flex; align-items: center; height: 38.3px; font-size: 23px; }
  .services__item svg { width: 20px; height: 20px; margin-right: 27px; flex: none; }

  .offer { position: absolute; left: 0; top: 480px; width: 474px; height: 56px; }
  .offer__text { position: absolute; left: 72px; top: 0; color: var(--green); font-size: 22px; line-height: 29px; letter-spacing: -.2px; }
  .offer__chevron { position: absolute; top: 17px; width: 24px; height: 40px; }
  .offer__chevron--left { left: 36px; }
  .offer__chevron--right { left: 416px; }

  .team-photo { position: absolute; left: 0; top: 462px; width: 474px; height: 261px;
    background: linear-gradient(180deg, #e9e9e9 0%, #d8d8d8 55%, #3a3a3a 56%, #2a2a2a 100%); }

  .contacts { position: absolute; left: 0; top: 743px; width: 474px; height: 131px; }
  .contacts__divider { position: absolute; left: 216px; top: 0; width: 1px; height: 131px; background: #9a9a9a; }
  .office { position: absolute; top: 0; }
  .office--bochum { left: 48px; }
  .office--herne { left: 253px; }
  .office__logo { position: relative; height: 52px; font-size: 13px; }
  .office__logo .brand { left: 0; top: 14px; }
  .office__logo .brand__mark { width: 12px; height: 12px; }
  .office__badge { display: block; width: 26px; height: 26px; background: var(--navy); flex: none; }
  .office__address { font-style: normal; font-size: 12px; line-height: 15.3px; margin-top: 13px; }
  .office__address .web { font-size: 11px; }
</style>
</head>
<body>

<section class="flyer flyer--front" aria-label="Vorderseite">
  <div class="front__photo" role="img" aria-label="Nebliger Wald mit Sonnenlicht zwischen hohen Bäumen und Regentropfen"></div>
  <div class="brand front__logo"><span class="brand__mark"></span>Lanberg Immobilien</div>
  <h1 class="front__question">Lauter Bäume?</h1>
  <p class="front__claim front__claim--one">Wir helfen Ihnen</p>
  <p class="front__note front__note--one">auch in den unsicheren Zeiten</p>
  <p class="front__claim front__claim--two">den Wald zu sehen</p>
  <p class="front__note front__note--two">...und bringen Licht in's Dunkel.</p>
  <div class="footer-band">Ihr Immobilienmakler aus Bochum</div>
</section>

<section class="flyer flyer--back" aria-label="Rückseite">
  <div class="brand back__logo"><span class="brand__mark"></span><span>Lanberg<br>Immobilien</span></div>
  <h2 class="services__title">Unsere<br>Dienstleistungen:</h2>
  <ul class="services__list">
    <li class="services__item"><svg viewBox="0 0 20 20"><rect x="1" y="3" width="16" height="16" fill="none" stroke="#6cb52d" stroke-width="2"/><path d="M4 10l4 5 9-13" fill="none" stroke="#6cb52d" stroke-width="2.4"/></svg>Verkauf</li>
    <li class="services__item"><svg viewBox="0 0 20 20"><rect x="1" y="3" width="16" height="16" fill="none" stroke="#6cb52d" stroke-width="2"/><path d="M4 10l4 5 9-13" fill="none" stroke="#6cb52d" stroke-width="2.4"/></svg>Wertgutachten</li>
    <li class="services__item"><svg viewBox="0 0 20 20"><rect x="1" y="3" width="16" height="16" fill="none" stroke="#6cb52d" stroke-width="2"/><path d="M4 10l4 5 9-13" fill="none" stroke="#6cb52d" stroke-width="2.4"/></svg>Vermietung</li>
    <li class="services__item"><svg viewBox="0 0 20 20"><rect x="1" y="3" width="16" height="16" fill="none" stroke="#6cb52d" stroke-width="2"/><path d="M4 10l4 5 9-13" fill="none" stroke="#6cb52d" stroke-width="2.4"/></svg>Wohnflächenberechnung</li>
    <li class="services__item"><svg viewBox="0 0 20 20"><rect x="1" y="3" width="16" height="16" fill="none" stroke="#6cb52d" stroke-width="2"/><path d="M4 10l4 5 9-13" fill="none" stroke="#6cb52d" stroke-width="2.4"/></svg>Energieausweis</li>
  </ul>

  <div class="offer" style="top:380px">
    <svg class="offer__chevron offer__chevron--left" viewBox="0 0 24 40"><path d="M4 2l16 18L4 38" fill="none" stroke="#6cb52d" stroke-width="7"/></svg>
    <p class="offer__text">Unser Erstgespräch kostet Sie nur<br>einen Kaffee und leckere Kekse.</p>
    <svg class="offer__chevron offer__chevron--right" viewBox="0 0 24 40"><path d="M20 2L4 20l16 18" fill="none" stroke="#6cb52d" stroke-width="7"/></svg>
  </div>

  <div class="team-photo" role="img" aria-label="Teamfoto mit fünf Mitarbeitenden in Weiß und Schwarz vor hellem Hintergrund"></div>

  <div class="contacts">
    <div class="office office--bochum">
      <div class="office__logo"><div class="brand"><span class="brand__mark"></span>Lanberg Immobilien</div></div>
      <address class="office__address">Lanberg Immobilien<br>Molvener Weg 417<br>44861 Bochum<br>0234 / 5550182<br><span class="web">www.lanberg-immobilien-beispiel.info</span></address>
    </div>
    <div class="contacts__divider"></div>
    <div class="office office--herne">
      <div class="office__logo"><div class="brand" style="color:var(--ink)">Kesu Immobilien<span class="office__badge"></span></div></div>
      <address class="office__address">Kesu Immobilien<br>Tillweg 27<br>44627 Herne<br>02325 / 555048<br><span class="web">www.kesu-beispiel.de</span></address>
    </div>
  </div>

  <div class="footer-band">...und Herne.</div>
</section>

</body>
</html>
```